Business Card for a Wedding Films Business

We require a business card design for our business 'Lewis Marrow Wedding Films'. The logo needs to look classy and high end.

Target Market(s)

Wedding Couples

Contact Information for Business Card

Lewis Marrow Wedding Films
07312 605 227
films@lewismarrowreels.com
www.lewismarrowreels.com

Facebook: @lewismarrowweddingfilms
Instagram: @lewismarrowfilms

Font styles to use
Sans Serif

Requirements
Must have
• Social media icons - Facebook and Instagram

```html
<!DOCTYPE html>
<html lang="en">
<head>
<meta charset="UTF-8">
<title>Lewis Marrow Wedding Films – Business Card</title>
<link href="https://fonts.googleapis.com/css2?family=Josefin+Sans:wght@400&family=Montserrat:wght@700&family=Raleway:wght@400&display=swap" rel="stylesheet">
<style>
  :root {
    --ink: #111111;
    --band: #000000;
    --handle: #c9ced3;
    --icon-tile: #b4bcc3;
    --sprocket-top: #a9b5bf;
    --sprocket-bottom: #7d8e9b;
    --photo-top: #2b5870;
    --photo-mid: #6f8c9c;
    --photo-table: #dfe3e6;
    --photo-low: #a7b1b8;
  }
  * { margin: 0; padding: 0; box-sizing: border-box; }
  html, body { width: 1200px; height: 737px; overflow: hidden; background: #ffffff; }
  .card { position: relative; width: 1200px; height: 737px; overflow: hidden; }

  .hero-photo {
    position: absolute; left: 0; top: 0; width: 1200px; height: 559px;
    background: linear-gradient(180deg, var(--photo-top) 0%, #3e6b81 22%, var(--photo-mid) 36%, var(--photo-table) 48%, #cdd3d7 70%, var(--photo-low) 100%);
  }

  .brand { position: absolute; right: 26px; top: 249px; text-align: right; font-family: "Josefin Sans", sans-serif; font-weight: 400; color: var(--ink); }
  .brand-name { font-size: 63px; letter-spacing: 9px; line-height: 1; white-space: nowrap; }
  .brand-tagline { font-size: 31px; letter-spacing: 13.5px; line-height: 1; margin-top: 12px; margin-right: 80px; white-space: nowrap; }

  .contact { position: absolute; left: 42px; font-family: "Montserrat", sans-serif; font-weight: 700; color: var(--ink); white-space: nowrap; line-height: 1; }
  .contact-phone { top: 382px; font-size: 31px; letter-spacing: 5px; }
  .contact-email { top: 438px; font-size: 27px; letter-spacing: 2.5px; text-transform: uppercase; }
  .contact-web { top: 494px; font-size: 27px; letter-spacing: 2.5px; text-transform: uppercase; }

  .social-band { position: absolute; left: 0; top: 559px; width: 1200px; height: 178px; background: var(--band); }
  .social { position: absolute; top: 32px; display: flex; align-items: center; gap: 10px; }
  .social-photos { left: 41px; }
  .social-community { left: 607px; }
  .social-tile { width: 70px; height: 70px; border-radius: 12px; background: var(--icon-tile); flex: none; }
  .social-handle { font-family: "Raleway", sans-serif; font-weight: 400; font-size: 28px; color: var(--handle); text-transform: uppercase; white-space: nowrap; letter-spacing: 0.5px; }

  .sprocket { position: absolute; top: 133px; width: 68px; height: 60px; border-radius: 8px; background: linear-gradient(180deg, var(--sprocket-top), var(--sprocket-bottom)); }
</style>
</head>
<body>
<main class="card">
  <div class="hero-photo" role="img" aria-label="Photograph of a silver wedding ring standing on a soft grey table against a blue-teal backdrop"></div>

  <div class="brand">
    <div class="brand-name">LEWIS MARROW</div>
    <div class="brand-tagline">WEDDING FILMS</div>
  </div>

  <div class="contact contact-phone">07312 605 227</div>
  <div class="contact contact-email">films@lewismarrowreels.com</div>
  <div class="contact contact-web">www.lewismarrowreels.com</div>

  <section class="social-band">
    <div class="social social-photos">
      <span class="social-tile"></span>
      <span class="social-handle">@lewismarrowfilms</span>
    </div>
    <div class="social social-community">
      <span class="social-tile"></span>
      <span class="social-handle">@lewismarrowweddingfilms</span>
    </div>

    <span class="sprocket" style="left:40px"></span>
    <span class="sprocket" style="left:230px"></span>
    <span class="sprocket" style="left:420px"></span>
    <span class="sprocket" style="left:610px"></span>
    <span class="sprocket" style="left:800px"></span>
    <span class="sprocket" style="left:989px"></span>
  </section>
</main>
</body>
</html>
```